New Company Business Card Design

I have a new company logo and I want a new business card design. I dont know if the logo file i attached is in the correct format or quality. We are a New York City Specialty construction Firm specializing in high risk out of the box projects. I want a simple and classy business card that people will his card is as crisp as the work his company does.

Target Market(s)

Clients in the heavy construction industry in New York City

Industry/Entity Type

Construction Company

Contact Information for Business Card

Simple Classy - DIFFERENT

Font styles to use
Other font styles liked:
• Mach the logo font in some way

Colors

Designer to choose colors to be used in the design.

Requirements
Must have
• Uniqueness
Nice to have
• Nothing particular - Just different and classy - Timeless
Should not have
• Goofy Shit or Gimmicky shit

```html
<!DOCTYPE html>
<html lang="en">
<head>
<meta charset="utf-8">
<title>Kestrel Ridge Builders – Business Card</title>
<link href="https://fonts.googleapis.com/css2?family=Lato:wght@400;700;900&display=swap" rel="stylesheet">
<style>
  :root{
    --brand-blue:#1160ab;
    --ink:#1d1d1f;
    --paper:#ffffff;
    --backdrop:#e4e5e7;
  }
  *{margin:0;padding:0;box-sizing:border-box}
  html,body{width:1200px;height:1200px;overflow:hidden;background:var(--backdrop);font-family:"Lato",sans-serif;color:var(--ink)}
  .card{position:absolute;left:180px;width:840px;height:480px;background:var(--paper);overflow:hidden;box-shadow:0 6px 18px rgba(0,0,0,.12)}
  .card--front{top:90px}
  .card--back{top:630px}

  .wordmark{position:absolute;display:flex;align-items:center;gap:12px;color:var(--brand-blue);font-weight:900;letter-spacing:.04em;text-transform:uppercase;line-height:1.05}
  .wordmark__square{width:26px;height:26px;background:var(--brand-blue);flex:none}
  .card--front .wordmark{left:0;right:0;top:150px;justify-content:center;font-size:40px}
  .skyline{position:absolute;left:0;right:0;bottom:0;height:170px;background:linear-gradient(180deg,#1466b4,var(--brand-blue))}

  .name-band{position:absolute;left:0;top:200px;width:430px;height:112px;background:var(--brand-blue);color:var(--paper);padding:22px 0 0 44px}
  .name-band__name{font-size:34px;font-weight:900;text-transform:uppercase;letter-spacing:.01em;line-height:1}
  .name-band__rule{height:2px;width:340px;background:var(--paper);margin:10px 0 6px}
  .name-band__title{font-size:19px;font-weight:400;text-transform:uppercase;letter-spacing:.02em}
  .edge-tab{position:absolute;right:0;top:70px;width:48px;height:90px;background:var(--brand-blue)}
  .card--back .wordmark{left:460px;top:200px;width:320px;font-size:30px}

  .contacts{position:absolute;left:44px;right:30px;bottom:70px;display:flex;align-items:center;font-size:19px}
  .contacts__group{padding:0 22px}
  .contacts__group:first-child{padding-left:0}
  .contacts__divider{width:2px;height:56px;background:var(--brand-blue)}
  .contacts__line{display:flex;align-items:center;gap:8px;line-height:1.45;white-space:nowrap}
  .contacts__line svg{width:16px;height:16px;fill:var(--brand-blue);flex:none}
</style>
</head>
<body>

<section class="card card--front" aria-label="Card front">
  <div class="wordmark"><span class="wordmark__square"></span><span>Kestrel Ridge<br>Builders, Inc.</span></div>
  <div class="skyline" role="img" aria-label="Blue city skyline silhouette with harbor statue"></div>
</section>

<section class="card card--back" aria-label="Card back">
  <div class="edge-tab"></div>
  <div class="name-band">
    <div class="name-band__name">Marcus T. Hollander</div>
    <div class="name-band__rule"></div>
    <div class="name-band__title">Founder</div>
  </div>
  <div class="wordmark"><span class="wordmark__square"></span><span>Kestrel Ridge<br>Builders, Inc.</span></div>

  <div class="contacts">
    <div class="contacts__group">
      <div class="contacts__line">
        <svg viewBox="0 0 16 16"><path d="M3.5 1l3 3-1.8 1.8a9 9 0 0 0 5.5 5.5L12 9.5l3 3-2 2C7 14.5 1.5 9 1.5 3z"/></svg>555-014-2231
      </div>
      <div class="contacts__line">
        <svg viewBox="0 0 16 16"><path d="M4 1h8v14H4zM5.5 3v9h5V3zM7 13h2v1H7z" fill-rule="evenodd"/></svg>555-017-8846
      </div>
    </div>
    <span class="contacts__divider"></span>
    <div class="contacts__group">
      <div class="contacts__line">
        <svg viewBox="0 0 16 16"><path d="M15 1L1 7l5 2 2 6z"/></svg>marcus@kestrelridge.com
      </div>
      <div class="contacts__line">
        <svg viewBox="0 0 16 16"><path d="M6.5 9.5l3-3M7 4.5l1.5-1.5a2.5 2.5 0 0 1 3.5 3.5L10.5 8M9 11.5L7.5 13A2.5 2.5 0 0 1 4 9.5L5.5 8" fill="none" stroke="#1160ab" stroke-width="1.8" stroke-linecap="round"/></svg>www.kestrelridge.com
      </div>
    </div>
    <span class="contacts__divider"></span>
    <div class="contacts__group">
      <div class="contacts__line">118 Harbor Point Road -</div>
      <div class="contacts__line">Linden Falls, New Jersey 07990</div>
    </div>
  </div>
</section>

</body>
</html>
```